IT Company based on Biology Business Needs a Business Card Design

We need a business card design for a new company called 'Lumen CELL'. We develop the machine learning solutions especially focused on deep learning algorithms for biology industry. Our initial product is a vision detection on biological images to help doctors diagnose the symptoms. We would like to see designs that use the color green.

Industry/Entity Type

Business

```html
<!DOCTYPE html>
<html lang="en">
<head>
<meta charset="utf-8">
<title>Lumen CELL – Business Card</title>
<link rel="stylesheet" href="https://fonts.googleapis.com/css2?family=Montserrat:wght@500;600&family=Nunito+Sans:wght@400&display=swap">
<style>
  :root {
    --bg: #e3e3e3;
    --card: #f4f4f4;
    --green: #6aac3a;
    --green-dark: #17863f;
    --ink: #2b2b2b;
    --ink-soft: #3d3d3d;
  }
  * { margin: 0; padding: 0; box-sizing: border-box; }
  html, body { width: 1200px; height: 900px; overflow: hidden; background: var(--bg); }
  .stage { position: relative; width: 1200px; height: 900px; }
  .card {
    position: absolute;
    width: 680px;
    height: 388px;
    background: var(--card);
    box-shadow: 0 2px 6px rgba(0,0,0,0.12);
    overflow: hidden;
  }
  .card-back { left: 70px; top: 36px; }
  .card-front { left: 450px; top: 476px; }
  .card-lines { position: absolute; inset: 0; width: 100%; height: 100%; }
  .brand {
    position: absolute;
    display: flex;
    align-items: center;
    gap: 12px;
    font-family: "Montserrat", sans-serif;
    font-weight: 500;
    color: var(--green);
    letter-spacing: -1px;
    white-space: nowrap;
  }
  .brand-dot { width: 26px; height: 26px; border-radius: 50%; background: var(--green); }
  .card-back .brand { left: 215px; top: 166px; font-size: 44px; }
  .card-front .brand { left: 50px; top: 250px; font-size: 40px; }
  .holder-name {
    position: absolute;
    left: 396px;
    top: 126px;
    font-family: "Montserrat", sans-serif;
    font-weight: 600;
    font-size: 30px;
    color: var(--ink);
    letter-spacing: 0.5px;
    white-space: nowrap;
  }
  .contact {
    position: absolute;
    left: 440px;
    font-family: "Nunito Sans", sans-serif;
    font-size: 14px;
    line-height: 18px;
    color: var(--ink-soft);
    white-space: nowrap;
  }
  .contact-address { top: 180px; }
  .contact-details { top: 226px; }
</style>
</head>
<body>
<main class="stage">

  <section class="card card-back" aria-label="Card back">
    <svg class="card-lines" viewBox="0 0 680 388" fill="none" stroke-width="2.5">
      <path stroke="var(--green)" d="M480 0 V128 Q480 140 468 140 H392 A13 13 0 0 0 392 166 H596 Q608 166 608 178 V388"/>
      <path stroke="var(--green-dark)" d="M30 388 V260 Q30 248 42 248 H118 A13 13 0 0 0 118 222 H-10"/>
    </svg>
    <div class="brand"><span class="brand-dot"></span>Lumen CELL</div>
  </section>

  <section class="card card-front" aria-label="Card front">
    <svg class="card-lines" viewBox="0 0 680 388" fill="none" stroke-width="2.5" stroke="var(--green)">
      <path d="M0 352 H376 Q388 352 388 340 V196 A16 16 0 0 1 420 196 V318 Q420 330 432 330 H680"/>
      <g class="contact-icons" fill="var(--ink)" stroke="none">
        <path d="M404 212 l8 7 h-3 v6 h-3 v-4 h-4 v4 h-3 v-6 h-3 z"/>
        <path d="M399 258 q2 -2 4 0 l2 3 q1 2 -1 3 q2 4 5 5 q1 -2 3 -1 l3 2 q2 2 0 4 q-2 2 -5 1 q-8 -4 -12 -12 q-1 -3 1 -5z"/>
        <rect x="398" y="283" width="16" height="11"/>
        <path d="M398 283 l8 6 l8 -6" stroke="var(--card)" stroke-width="1.4" fill="none"/>
      </g>
      <g stroke="var(--ink)" stroke-width="1.3">
        <circle cx="406" cy="311" r="7"/>
        <ellipse cx="406" cy="311" rx="3" ry="7"/>
        <path d="M399 311 H413 M400.5 307 H411.5 M400.5 315 H411.5"/>
      </g>
    </svg>
    <div class="brand"><span class="brand-dot"></span>Lumen CELL</div>
    <h1 class="holder-name">ALEX REED</h1>
    <p class="contact contact-address">Address Line 1<br>Address Line 2</p>
    <p class="contact contact-details">123 555 789<br>alex.reed@lumencell.com<br>www.lumencell.com</p>
  </section>

</main>
</body>
</html>
```